Pouch for cosmetic ingredients

We need a design for a 16oz pouch (with bottom) that can be used to package a variety of different cosmetic ingredients and chemicals in powder form (or granules / pastilles / flakes).
Our corporate colors are Sage (CMYK: 10, 6, 28, 20) and Orange (CMYK: 1, 75, 100, 8), but we are open to add additional colors. The label with the description of the product goes on the back of the pouch, whereas the front will have a window where the product can be seen.

Cosmetic

```html
<!DOCTYPE html>
<html lang="en">
<head>
<meta charset="utf-8">
<title>16oz Stand Up Pouch – Label Layout</title>
<link rel="stylesheet" href="https://fonts.googleapis.com/css2?family=Arimo:wght@400;700&family=Source+Sans+3:wght@400;600&display=swap">
<style>
  :root {
    --paper: #ffffff;
    --ink: #111111;
    --spec-red: #e0202a;
    --pouch-black: #000000;
    --sage: #bfbb9e;
    --orange: #e0601f;
    --swatch-gold: #e2ab17;
    --swatch-silver: #cfd0d2;
    --swatch-red: #b01e2d;
    --swatch-kraft: #c9ad72;
    --rule: #555555;
  }
  html, body { margin: 0; padding: 0; overflow: hidden; background: var(--paper); }
  .sheet { display: block; width: 933px; height: 1200px; }
  .spec { font-family: "Arimo", Arial, sans-serif; fill: var(--ink); }
  .spec-bold { font-weight: 700; }
  .spec-red { fill: var(--spec-red); font-weight: 700; }
  .swatch-label { font-family: "Arimo", Arial, sans-serif; font-size: 3.2px; font-weight: 700; fill: var(--ink); }
  .panel-title { font-family: "Arimo", Arial, sans-serif; font-weight: 700; font-size: 11px; fill: var(--ink); }
  .dimension { font-family: "Arimo", Arial, sans-serif; font-size: 7px; fill: var(--ink); }
  .dimension-line { stroke: var(--rule); stroke-width: 0.6; fill: none; }
  .pouch-black { fill: var(--pouch-black); }
  .window { fill: var(--paper); stroke: var(--ink); stroke-width: 0.6; }
  .product-name { font-family: "Source Sans 3", sans-serif; font-size: 20px; fill: var(--paper); }
  .brand-name { font-family: "Source Sans 3", sans-serif; font-size: 22px; font-weight: 400; fill: var(--orange); }
  .brand-tagline { font-family: "Source Sans 3", sans-serif; font-size: 10.5px; fill: var(--paper); }
  .back-label { fill: var(--sage); }
  .description { font-family: "Source Sans 3", sans-serif; font-size: 13.6px; fill: var(--ink); }
</style>
</head>
<body>
<svg class="sheet" viewBox="0 0 600 771.7" xmlns="http://www.w3.org/2000/svg">
  <defs>
    <linearGradient id="artwork-tone" x1="0" y1="0" x2="0" y2="1">
      <stop offset="0" stop-color="#bfbb9e" stop-opacity="0"/>
      <stop offset="0.45" stop-color="#e0601f" stop-opacity="0.75"/>
      <stop offset="1" stop-color="#e0601f"/>
    </linearGradient>
  </defs>

  <!-- Colour options -->
  <g class="color-options">
    <text class="spec spec-red" x="47" y="13" font-size="5">AVAILABLE IN 13 DIFFERENT COLORS:</text>
    <text class="swatch-label" x="52" y="19">Gold</text>
    <text class="swatch-label" x="83" y="19">Silver</text>
    <text class="swatch-label" x="117" y="19">Black</text>
    <text class="swatch-label" x="148" y="19">Red 187</text>
    <text class="swatch-label" x="182" y="19">Clear</text>
    <text class="swatch-label" x="205" y="19">Natural Kraft</text>
    <rect x="47" y="24" width="22" height="20" fill="var(--swatch-gold)"/>
    <rect x="80" y="24" width="22" height="20" fill="var(--swatch-silver)"/>
    <rect x="113" y="24" width="22" height="20" fill="var(--pouch-black)"/>
    <rect x="146" y="24" width="22" height="20" fill="var(--swatch-red)"/>
    <rect x="179" y="24" width="22" height="20" fill="var(--paper)"/>
    <rect x="212" y="24" width="22" height="20" fill="var(--swatch-kraft)"/>

    <text class="swatch-label" x="47" y="57">Clear/Black</text>
    <text class="swatch-label" x="81" y="57">Clear/Gold</text>
    <text class="swatch-label" x="113" y="57">Clear/Silver</text>
    <text class="swatch-label" x="151" y="57">White</text>
    <text class="swatch-label" x="180" y="57">Matte Black</text>
    <text class="swatch-label" x="213" y="57">Matte White</text>
    <rect x="47" y="61" width="22" height="20" fill="var(--paper)" stroke="#999" stroke-width="0.4"/>
    <polygon points="47,81 69,61 69,81" fill="var(--pouch-black)"/>
    <rect x="80" y="61" width="22" height="20" fill="var(--paper)" stroke="#999" stroke-width="0.4"/>
    <polygon points="80,81 102,61 102,81" fill="var(--swatch-gold)"/>
    <rect x="113" y="61" width="22" height="20" fill="var(--paper)" stroke="#999" stroke-width="0.4"/>
    <polygon points="113,81 135,61 135,81" fill="var(--swatch-silver)"/>
    <rect x="146" y="61" width="22" height="20" fill="var(--paper)" stroke="#999" stroke-width="0.4"/>
    <rect x="179" y="61" width="22" height="20" fill="var(--pouch-black)"/>
    <rect x="212" y="61" width="22" height="20" fill="var(--paper)" stroke="#999" stroke-width="0.4"/>
  </g>

  <!-- Specification -->
  <g class="specification">
    <text class="spec spec-bold" x="47" y="119" font-size="7">PBY1.13</text>
    <text class="spec spec-bold" x="47" y="128" font-size="7">16oz Stand Up Pouch</text>
    <text class="spec" x="47" y="138" font-size="5">size: 7" W x 11-1/2" H + 4" G</text>
    <text class="spec" x="47" y="148" font-size="5">size: 178mm W x 292mm H + 102mm G</text>
    <text class="spec" x="47" y="157" font-size="5">Imprint Area: 5.50" x 5.00"</text>
    <text class="spec spec-red" x="337" y="119" font-size="5">Imprint Size:</text>
    <text class="spec spec-red" x="337" y="126" font-size="5">Imprint Color:</text>
    <text class="spec spec-red" x="337" y="134" font-size="5">Product Color:</text>
  </g>

  <!-- Front panel -->
  <g class="front">
    <text class="panel-title" x="180" y="187" text-anchor="middle">FRONT</text>
    <line class="dimension-line" x1="59" y1="204" x2="300" y2="204"/>
    <rect x="158" y="196" width="44" height="10" fill="var(--paper)"/>
    <text class="dimension" x="180" y="203" text-anchor="middle">7.00"</text>

    <line class="dimension-line" x1="43" y1="208" x2="43" y2="745"/>
    <line class="dimension-line" x1="38" y1="208" x2="56" y2="208"/>
    <line class="dimension-line" x1="38" y1="606" x2="56" y2="606"/>
    <line class="dimension-line" x1="38" y1="745" x2="56" y2="745"/>
    <rect x="39" y="390" width="8" height="36" fill="var(--paper)"/>
    <text class="dimension" transform="translate(46 408) rotate(-90)" text-anchor="middle">11-1/2"</text>
    <rect x="39" y="662" width="8" height="26" fill="var(--paper)"/>
    <text class="dimension" transform="translate(46 675) rotate(-90)" text-anchor="middle">4.00"</text>

    <rect class="pouch-black" x="59" y="208" width="241" height="398" rx="10"/>
    <rect class="pouch-black" x="59" y="607" width="241" height="138" rx="10"/>

    <text class="product-name" x="180" y="298" text-anchor="middle">[Product Name]</text>
    <rect class="window" x="86" y="316" width="188" height="171"/>

    <g class="brand">
      <rect x="76" y="549" width="14" height="14" fill="var(--orange)"/>
      <text class="brand-name" x="96" y="570">Fernleaf Cosmetics</text>
      <text class="brand-tagline" x="180" y="584" text-anchor="middle">Specializing in Cosmetic Ingredients since 1997.</text>
    </g>
  </g>

  <!-- Back panel -->
  <g class="back">
    <text class="panel-title" x="459" y="187" text-anchor="middle">BACK</text>
    <text class="dimension" x="336" y="198" font-size="5">3/16"</text>
    <text class="dimension" x="570" y="198" font-size="5">3/16"</text>
    <text class="dimension" x="316" y="228" font-size="5">15/16"</text>
    <text class="dimension" x="320" y="254" font-size="5">9/16"</text>
    <line class="dimension-line" x1="331" y1="208" x2="331" y2="260"/>

    <rect class="back-label" x="338" y="208" width="242" height="399" rx="8"/>
    <rect x="338" y="345" width="242" height="262" rx="8" fill="url(#artwork-tone)"
          role="img" aria-label="Orange line illustration of a mortar and pestle"/>

    <g class="description">
      <text x="350" y="290">[Product description here.Product</text>
      <text x="350" y="308">description here.Product</text>
      <text x="350" y="326">description here.Product descrip-</text>
      <text x="350" y="344">tion here.Product description</text>
      <text x="396" y="362">here.Product description</text>
      <text x="401" y="380">here.Product description</text>
      <text x="405" y="398">here.Product description</text>
      <text x="425" y="416">here.Product descrip-</text>
      <text x="453" y="434">tion here.]</text>
    </g>
  </g>
</svg>
</body>
</html>
```